We need a letterhead incorporating our logo (uploaded file), with the name of our organization (Dunmore Hollis County Police Association) and our slogan (Strength in Unity). Dark blue should be incorporated somewhere in the design, either the font color or elsewhere. Please make sure our logo is included in the design. The organization is a law enforcement union type group.

Target Market(s)

Members of our association, policticians, and anyone receiving our letters

Colors
0255a3

Requirements
Must have
• Our logo, Association name, and slogan.
Nice to have
• A professional and eye-catching letterhead design incorporating the logo, name, and slogan.

```html
<!DOCTYPE html>
<html lang="en">
<head>
<meta charset="utf-8">
<title>Dunmore Hollis County Police Association – Letterhead</title>
<link href="https://fonts.googleapis.com/css2?family=Cinzel:wght@500&family=Montserrat:wght@500;600;700&family=Open+Sans:wght@400;600&family=Great+Vibes&display=swap" rel="stylesheet">
<style>
  :root{
    --brand-blue:#0255a3;
    --accent-gold:#f7b95c;
    --paper:#ffffff;
    --backdrop:#e9e9ea;
    --ink:#2a2a2a;
    --ink-soft:#8a8f99;
  }
  html,body{margin:0;width:1200px;height:1200px;overflow:hidden;background:var(--backdrop);}
  .letterhead{position:absolute;left:160px;top:30px;width:880px;height:1140px;background:var(--paper);
    box-shadow:0 2px 10px rgba(0,0,0,.12);overflow:hidden;}
  .letterhead-art{position:absolute;inset:0;}
  .recipient{position:absolute;left:80px;top:330px;font-family:"Montserrat",sans-serif;}
  .recipient .label{font-size:12px;color:var(--ink);}
  .recipient .name{font-size:20px;font-weight:700;color:var(--brand-blue);margin:2px 0;}
  .recipient .line{font-size:11px;color:var(--ink);font-weight:500;}
  .date{position:absolute;right:90px;top:250px;font-family:"Montserrat",sans-serif;font-size:12px;color:var(--ink);}
  .date b{color:var(--brand-blue);}
  .letter-flow{position:absolute;left:80px;top:430px;width:540px;}
  .letter-body{font-family:"Open Sans",sans-serif;font-size:12px;line-height:1.6;color:var(--ink);}
  .letter-body p{margin:0 0 14px;}
  .letter-body .intro,.letter-body .closing{color:var(--ink-soft);}
  .signature{width:260px;margin-top:26px;}
  .signature .script{font-family:"Great Vibes",cursive;font-size:42px;line-height:1.1;color:#111;padding-left:20px;}
  .signature .rule{border-top:1.5px solid #222;margin-top:4px;}
  .signature .role{font-family:"Montserrat",sans-serif;font-weight:700;font-size:11px;letter-spacing:.5px;margin-top:8px;color:#111;}
</style>
</head>
<body>
<main class="letterhead">
  <svg class="letterhead-art" width="880" height="1140" viewBox="0 0 880 1140">
    <path class="header-band" d="M0 0 H520 C420 110 260 230 0 270 Z" fill="var(--brand-blue)"/>
    <path class="header-stripe" d="M530 0 C430 118 265 240 0 282 L0 272 C262 232 424 112 516 0 Z" fill="var(--accent-gold)"/>
    <g class="org-title" transform="translate(40 225) rotate(-30)" fill="#fff">
      <text font-family="Cinzel, serif" font-weight="500" font-size="25" x="0" y="0">DUNMORE HOLLIS COUNTY</text>
      <text font-family="Montserrat, sans-serif" font-weight="700" font-size="20" letter-spacing="1.5" x="40" y="30">POLICE ASSOCIATION</text>
    </g>
    <g class="org-mark">
      <circle cx="400" cy="190" r="64" fill="#fff" stroke="var(--brand-blue)" stroke-width="4"/>
      <text font-family="Montserrat, sans-serif" font-weight="700" font-size="13" fill="var(--brand-blue)" text-anchor="middle">
        <tspan x="400" y="186">DUNMORE</tspan><tspan x="400" y="204">HOLLIS</tspan>
      </text>
    </g>
    <path class="footer-band" d="M880 600 C700 760 520 960 410 1140 H880 Z" fill="var(--brand-blue)"/>
    <path class="footer-stripe" d="M880 614 C706 772 530 968 424 1140 L432 1140 C538 970 712 778 880 624 Z" fill="var(--accent-gold)"/>
    <g class="footer-text" font-family="Montserrat, sans-serif">
      <text transform="translate(520 1060) rotate(-40)" font-size="26" font-weight="700" letter-spacing="2" fill="#fff">STRENGTH IN UNITY</text>
      <text transform="translate(540 1082) rotate(-40)" font-size="12" font-weight="500" fill="#fff"><tspan fill="var(--accent-gold)" font-weight="700">P:</tspan> 555.014.2210  |  <tspan fill="var(--accent-gold)" font-weight="700">F:</tspan> 555.014.2211</text>
      <text transform="translate(558 1102) rotate(-40)" font-size="12" font-weight="500" fill="#fff"><tspan fill="var(--accent-gold)" font-weight="700">E:</tspan> info@dhcpa-union.org  |  <tspan fill="var(--accent-gold)" font-weight="700">W:</tspan> www.dhcpa-union.org</text>
      <text transform="translate(576 1122) rotate(-40)" font-size="12" font-weight="500" fill="var(--accent-gold)">42 HARROW LANE, DUNMORE HOLLIS 20145</text>
    </g>
  </svg>

  <div class="date"><b>Date:</b> 24-03-2018</div>

  <div class="recipient">
    <div class="label">To</div>
    <div class="name">Alan Reyes</div>
    <div class="line">CEO, <b>NORTHFIELD STUDIO</b></div>
    <div class="line"><b>W:</b> www.northfieldstudio.com</div>
  </div>

  <div class="letter-flow">
    <section class="letter-body">
      <p class="intro">Lorem ipsum dolor sit amet, consectetur adipiscing elit. Pellentesque dictum, ante non ullamcorper convallis, nunc quam blandit metus, ac mollis eros felis a orci. Donec congue, mauris ut pulvinar lobortis, dolor massa feugiat nisi, at tincidunt metus leo vel elit. Proin facilisis semper lobortis. Vivamus augue purus, cursus quis urna non, accumsan pellentesque est. Nulla in iaculis magna, quis aliqu et ex. Cras efficitur metus eget purus euismod facilisis. Proin non metus tincidunt, auctor ipsum a, tempor mi.</p>
      <p>Nulla egestas vulputate risus, ut vestibulum diam commodo id. Mauris ornare libero eu erat porttitor ultrices. Proin sed lectus scelerisque ligula bibendum sagittis ac nec leo. Donec ac accumsan diam, et lobortis mauris.</p>
      <p>Nulla congue volutpat nisl ac lobortis. Integer dignissim interdum libero, quis feugiat velit pretium at. Phasellus sit amet libero rutrum, feugiat odio et, tempus purus. Cras ultricies, leo at fringilla solli cit udin, leo sapien placerat enim, a rutrum lorem enim ut tortor. Phasellus magna ante, cong ue maximus egestas sit amet, venenatis scelerisque felis.</p>
      <p class="closing">Nulla congue volutpat nisl ac lobortis. Integer dignissim interdum libero, quis feugiat velit pretium at. Phasellus sit amet libero rutrum, feugiat odio et, tempus purus. Cras ultricies, leo at fringilla solli cit udin, leo sapien placerat enim, a rutrum lorem enim ut tortor. Phasellus magna ante, cong ue maximus egestas sit amet, venenatis scelerisque felis.</p>
    </section>

    <div class="signature">
      <div class="script">Alan Reyes</div>
      <div class="rule"></div>
      <div class="role">DESIGNATION PLACE HERE</div>
    </div>
  </div>
</main>
</body>
</html>
```